Update Wordpress website to be captivating, modern and concise

Help us create a cohesive brand and deliver our marketing messages more concisely. We would like to update our Wordpress website to be clean, modern and captivating. Please see the uploaded file for more information on our company, our current website and how we want to continue the relationship beyond the contest. Thank you and we look forward to receiving your creative ideas!

Update: We no longer need you to complete the development.
Updates

We no longer require you to implement the design in Wordpress. Please provide your best, creative designs. Thanks

Target Market(s)

Our customers are companies who are looking for sleek, sexy, easy to use mobile applications for their sales teams. Our customers range from your small to Pinnacle 300.

Industry/Entity Type

Marketing

Font styles to use
Sans Serif

Requirements
Must have
• Clean, contemporary, engaging. Comes across as easy to use and inviting. Use the blue in our logo. We do a lot of work on Veltra Apps and therefore our standard is the Veltra UX for our styling and UI.
Should not have
• Clutter and distracting.

```html
<!DOCTYPE html>
<html lang="en">
<head>
<meta charset="utf-8">
<title>Fluent Metrics</title>
<link href="https://fonts.googleapis.com/css2?family=Montserrat:wght@300;400;500;600&display=swap" rel="stylesheet">
<style>
:root{
  --blue:#2b8ff0;
  --blue-soft:#4aa3ea;
  --ink:#222;
  --text:#555;
  --muted:#8a8a8a;
  --card:#e9e9e9;
  --tint:#f4f9fe;
  --foot:#fafafa;
  --white:#fff;
}
*{margin:0;padding:0;box-sizing:border-box}
html,body{width:1200px;height:2479px;overflow:hidden;background:var(--white)}
body{position:relative;font-family:"Montserrat",sans-serif;color:var(--ink)}
.abs{position:absolute}
.center{left:0;width:1200px;text-align:center}

/* header */
.site-header{top:0;left:0;width:1200px;height:84px;background:var(--white)}
.brand{left:160px;top:18px;display:flex;align-items:center;gap:10px}
.brand-dot{width:46px;height:46px;border-radius:50%;background:var(--blue)}
.brand-name{font-size:22px;font-weight:600;line-height:22px;color:#444;width:120px}
.nav{top:33px;font-size:15px;color:#555}
.nav.active{color:#111;font-weight:500}
.search-box{left:970px;top:0;width:68px;height:84px;background:var(--blue)}

/* hero */
.hero{top:84px;left:0;width:1200px;height:585px;background:linear-gradient(160deg,#3e3a38 0%,#2a2827 45%,#4a4541 100%)}
.hero-title{top:258px;font-size:50px;font-weight:500;color:var(--white)}
.hero-text{top:323px;font-size:17px;line-height:22px;color:#eee;font-weight:400}
.hero-btn{left:512px;top:397px;width:176px;height:43px;background:var(--blue);color:var(--white);font-size:17px;line-height:43px;text-align:center}

/* section titles */
.section-title{font-size:42px;font-weight:300;color:var(--ink)}
.section-title .num{color:var(--blue);font-size:50px}
.section-sub{font-size:28px;font-weight:300;color:#444}
.rule{height:1px;background:#e4e4e4}

/* solution cards */
.card{width:162px;height:163px;background:var(--card);border-radius:6px;text-align:center;font-size:17px;line-height:22px;color:#555}
.card svg{display:block;margin:24px auto 14px}
.card b{display:block;font-weight:500;color:var(--blue-soft)}
.card.active{background:var(--blue-soft);color:var(--white)}
.card.active b{color:var(--white)}

/* challenge */
.challenge{top:1091px;left:0;width:1200px;height:722px;background:var(--tint)}
.tablet{left:451px;top:1299px;width:301px;height:442px;border-radius:24px;background:linear-gradient(180deg,#f4f4f4,#e2e4e6);border:2px solid #cfd2d5}
.tablet-screen{left:466px;top:1340px;width:271px;height:358px;background:linear-gradient(180deg,#2ea3d9 0%,#2ea3d9 22%,#f5f7f9 22%,#f5f7f9 78%,#2e3a45 78%,#2e3a45 82%,#f5f7f9 82%)}
.feature{width:220px;font-size:13px;line-height:18px;color:#777}
.feature h3{font-size:23px;font-weight:400;color:var(--blue-soft);margin-bottom:6px;display:flex;align-items:center;gap:8px}
.feature .more{display:block;font-size:12px;color:#222;font-weight:500}
.feature.left{text-align:right}
.feature.left h3{justify-content:flex-end}
.feature.right .more{text-align:right}

/* band */
.band{top:1813px;left:0;width:1200px;height:113px;background:var(--blue);color:var(--white);font-size:33px;font-weight:300;line-height:113px;text-align:center}

/* partners */
.partner{width:150px;height:46px;border-radius:6px;background:#d6d6d6}
.arrow-btn{width:30px;height:30px}

/* footer */
.footer{top:2210px;left:0;width:1200px;height:269px;background:var(--foot)}
.foot-col{top:2250px;font-size:12px;line-height:24px;color:#666}
.foot-col h4{font-size:13px;font-weight:600;color:#333;margin-bottom:8px}
.copyright{top:2444px;left:160px;font-size:12px;color:#777}
</style>
</head>
<body>

<header class="abs site-header">
  <div class="abs brand"><span class="brand-dot"></span><span class="brand-name">Fluent Metrics</span></div>
  <span class="abs nav active" style="left:605px">Home</span>
  <span class="abs nav" style="left:679px">Blog</span>
  <span class="abs nav" style="left:744px">About Us</span>
  <span class="abs nav" style="left:840px">Join The Team</span>
  <div class="abs search-box">
    <svg width="68" height="84" viewBox="0 0 68 84"><circle cx="32" cy="40" r="8" fill="none" stroke="#fff" stroke-width="2.5"/><line x1="38" y1="46" x2="44" y2="52" stroke="#fff" stroke-width="3"/></svg>
  </div>
</header>

<section class="abs hero" role="img" aria-label="Dimmed photo of people meeting at a table with a coffee cup, phone and tablet"></section>
<h1 class="abs center hero-title">Drive Action And Results</h1>
<p class="abs center hero-text">Lorem ipsum dolor sit amet, consectetuer adipiscing elit, sed diam<br>nonummy nibh euismod tincidunt ut laoreet dolore magna.</p>
<a class="abs hero-btn">How it Works</a>
<svg class="abs" style="left:578px;top:600px" width="44" height="56" viewBox="0 0 44 56">
  <rect x="10" y="10" width="26" height="40" rx="13" fill="#fff"/>
  <line x1="23" y1="10" x2="23" y2="26" stroke="#555" stroke-width="1.5"/>
  <line x1="10" y1="26" x2="36" y2="26" stroke="#555" stroke-width="1.5"/>
  <path d="M4 18 q2 -10 12 -12" fill="none" stroke="#fff" stroke-width="2"/>
</svg>

<h2 class="abs center section-title" style="top:718px">TOP <span class="num">20</span> MOST PROMISING Data</h2>
<div class="abs rule" style="left:295px;top:805px;width:150px"></div>
<div class="abs rule" style="left:755px;top:805px;width:150px"></div>
<p class="abs center section-sub" style="top:780px">Analytics Company</p>

<div class="abs card" style="left:198px;top:868px">
  <svg width="60" height="50" viewBox="0 0 60 50"><path d="M6 18h48l-6 28H12z" fill="var(--blue-soft)"/><path d="M16 18l8-14M44 18l-8-14" stroke="var(--blue-soft)" stroke-width="4" fill="none"/><path d="M22 26v12M30 26v12M38 26v12" stroke="#e9e9e9" stroke-width="3"/></svg>
  <b>Order</b>Management
</div>
<div class="abs card active" style="left:412px;top:868px">
  <svg width="60" height="50" viewBox="0 0 60 50"><path d="M30 2l8 16 18 2-13 12 4 18-17-9-17 9 4-18L4 20l18-2z" fill="#fff"/></svg>
  <b>Goal</b>Manager
</div>
<div class="abs card" style="left:626px;top:868px">
  <svg width="60" height="54" viewBox="0 0 60 54"><path d="M30 2l26 12v26L30 52 4 40V14z" fill="var(--blue-soft)"/><path d="M4 14l26 12 26-12M30 26v26" stroke="#e9e9e9" stroke-width="2.5" fill="none"/></svg>
  <b>Sale</b>Enablement
</div>
<div class="abs card" style="left:840px;top:868px">
  <svg width="60" height="50" viewBox="0 0 60 50"><circle cx="30" cy="25" r="22" fill="none" stroke="var(--blue-soft)" stroke-width="5"/><line x1="30" y1="25" x2="42" y2="14" stroke="var(--blue-soft)" stroke-width="4"/><circle cx="30" cy="25" r="4" fill="var(--blue-soft)"/></svg>
  <b>Insight</b>POP
</div>

<section class="abs challenge"></section>
<h2 class="abs center section-title" style="top:1140px">Wins Wholesale Industry Solution</h2>
<div class="abs rule" style="left:300px;top:1223px;width:170px"></div>
<div class="abs rule" style="left:730px;top:1223px;width:170px"></div>
<p class="abs center section-sub" style="top:1200px">App Challenge</p>

<div class="abs tablet"></div>
<div class="abs tablet-screen" role="img" aria-label="Tablet screen showing a preview of the website home page"></div>

<svg class="abs" style="left:0;top:1380px" width="1200" height="330" viewBox="0 0 1200 330">
  <g stroke="#8fa3b5" stroke-width="1.2" stroke-dasharray="4 4" fill="none">
    <line x1="399" y1="32" x2="451" y2="52"/><line x1="399" y1="154" x2="451" y2="154"/><line x1="399" y1="273" x2="451" y2="255"/>
    <line x1="752" y1="52" x2="799" y2="26"/><line x1="752" y1="147" x2="799" y2="147"/><line x1="752" y1="255" x2="799" y2="266"/>
  </g>
  <g fill="#fff" stroke="var(--blue-soft)" stroke-width="2">
    <circle cx="393" cy="32" r="6"/><circle cx="393" cy="154" r="6"/><circle cx="393" cy="273" r="6"/>
    <circle cx="805" cy="26" r="6"/><circle cx="805" cy="147" r="6"/><circle cx="805" cy="266" r="6"/>
  </g>
</svg>

<div class="abs feature left" style="left:124px;top:1396px">
  <h3>Whole Sale <svg width="34" height="24" viewBox="0 0 34 24"><rect x="1" y="3" width="20" height="14" fill="none" stroke="currentColor" stroke-width="2"/><path d="M21 7h7l5 5v5H21z" fill="none" stroke="currentColor" stroke-width="2"/><circle cx="8" cy="20" r="3" fill="#fff" stroke="currentColor" stroke-width="2"/><circle cx="27" cy="20" r="3" fill="#fff" stroke="currentColor" stroke-width="2"/></svg></h3>
  Lorem Ipsum Dolor Sit Amet,<br>Consectetuer Adipiscing Elit.<span class="more">Discover &gt;&gt;</span>
</div>
<div class="abs feature left" style="left:124px;top:1518px">
  <h3>Capacity <svg width="26" height="26" viewBox="0 0 26 26"><circle cx="13" cy="13" r="5" fill="none" stroke="currentColor" stroke-width="2"/><circle cx="13" cy="13" r="10" fill="none" stroke="currentColor" stroke-width="2" stroke-dasharray="4 3"/></svg></h3>
  Lorem Ipsum Dolor Sit Amet,<br>Consectetuer Adipiscing Elit.<span class="more">Discover &gt;&gt;</span>
</div>
<div class="abs feature left" style="left:124px;top:1650px">
  <h3>Whole Sale <svg width="34" height="24" viewBox="0 0 34 24"><rect x="1" y="3" width="20" height="14" fill="none" stroke="currentColor" stroke-width="2"/><path d="M21 7h7l5 5v5H21z" fill="none" stroke="currentColor" stroke-width="2"/><circle cx="8" cy="20" r="3" fill="#fff" stroke="currentColor" stroke-width="2"/><circle cx="27" cy="20" r="3" fill="#fff" stroke="currentColor" stroke-width="2"/></svg></h3>
  Lorem Ipsum Dolor Sit Amet,<br>Consectetuer Adipiscing Elit.<span class="more">Discover &gt;&gt;</span>
</div>

<div class="abs feature right" style="left:856px;top:1390px">
  <h3><svg width="28" height="24" viewBox="0 0 28 24"><rect x="1" y="5" width="26" height="18" rx="3" fill="none" stroke="currentColor" stroke-width="2"/><path d="M9 5V1h10v4M1 12h26" fill="none" stroke="currentColor" stroke-width="2"/></svg>Sol. Selling</h3>
  Lorem Ipsum Dolor Sit Amet,<br>Consectetuer Adipiscing Elit.<span class="more">Discover &gt;&gt;</span>
</div>
<div class="abs feature right" style="left:856px;top:1514px">
  <h3><svg width="26" height="24" viewBox="0 0 26 24"><circle cx="4" cy="20" r="3" fill="currentColor"/><path d="M2 11a11 11 0 0 1 11 11M2 3a19 19 0 0 1 19 19" fill="none" stroke="currentColor" stroke-width="3"/></svg>Mobile</h3>
  Lorem Ipsum Dolor Sit Amet,<br>Consectetuer Adipiscing Elit.<span class="more">Discover &gt;&gt;</span>
</div>
<div class="abs feature right" style="left:856px;top:1644px">
  <h3><svg width="28" height="24" viewBox="0 0 28 24"><rect x="1" y="5" width="26" height="18" rx="3" fill="none" stroke="currentColor" stroke-width="2"/><path d="M9 5V1h10v4M1 12h26" fill="none" stroke="currentColor" stroke-width="2"/></svg>Sol. Selling</h3>
  Lorem Ipsum Dolor Sit Amet,<br>Consectetuer Adipiscing Elit.<span class="more">Discover &gt;&gt;</span>
</div>

<div class="abs band">Showcased at Nimbus Core Startup Forum</div>

<h2 class="abs center section-title" style="top:1970px;font-size:38px">Featured Partner</h2>
<div class="abs rule" style="left:440px;top:2047px;width:60px"></div>
<div class="abs rule" style="left:700px;top:2047px;width:60px"></div>
<p class="abs center section-sub" style="top:2028px;font-size:25px">Lorem a dummy</p>

<svg class="abs arrow-btn" style="left:130px;top:2117px" viewBox="0 0 30 30"><circle cx="15" cy="15" r="13" fill="none" stroke="#bbb" stroke-width="2"/><path d="M17 9l-6 6 6 6" fill="none" stroke="#bbb" stroke-width="2"/></svg>
<div class="abs partner" style="left:231px;top:2109px"></div>
<div class="abs partner" style="left:441px;top:2109px"></div>
<div class="abs partner" style="left:649px;top:2109px"></div>
<div class="abs partner" style="left:864px;top:2103px;width:100px;height:58px;border-radius:0"></div>
<svg class="abs arrow-btn" style="left:1037px;top:2117px" viewBox="0 0 30 30"><circle cx="15" cy="15" r="13" fill="none" stroke="#333" stroke-width="2"/><path d="M13 9l6 6-6 6" fill="none" stroke="#333" stroke-width="2"/></svg>

<footer class="abs footer"></footer>
<div class="abs foot-col" style="left:160px"><h4>Website Links</h4>Home<br>About Us<br>Blogs<br>Contact</div>
<div class="abs foot-col" style="left:385px"><h4>Site Map</h4>Privacy<br>Policy<br>About us<br>Terms &amp; Condition<br>Faq</div>
<div class="abs foot-col" style="left:625px"><h4>Social Links</h4>Friendbook<br>Chirper<br>LinkUp<br>Circles +<br>Streamtube</div>
<div class="abs foot-col" style="left:833px"><h4>Contact Us</h4>48 Harbor Lane, Suite 210<br>Pinecrest, UT 84010<br>Ph: 555 010 2020<br>Email: info@fluentmetrics.example<br>www.fluentmetrics.example</div>
<div class="abs rule" style="left:160px;top:2428px;width:880px"></div>
<p class="abs copyright">©2014 Fluent Metrics.</p>

</body>
</html>
```